R5 Construction USA

We are General Contractors performing Federal Contracting two generations, website with one page our 'Capability Statement", five page website, want to as soon as possible secure page and Under Construction with R5 logo. No files to upload yet, time to assemble.

Coding

Coded - Design and coding required

Number of Pages Required

1 page

```html
<!DOCTYPE html>
<html lang="en">
<head>
<meta charset="UTF-8">
<title>R5 Construction USA — Federal Contracting</title>
<link href="https://fonts.googleapis.com/css2?family=Inter:wght@400;500;600;700;800&display=swap" rel="stylesheet">
<style>
:root{
  --red:#c81f3c;
  --red-dark:#a8172f;
  --navy:#14213a;
  --navy-2:#1b2b4a;
  --ink:#1a1d24;
  --muted:#5f6570;
  --line:#e4e6ea;
  --soft:#f2f2f3;
  --white:#ffffff;
}
*{box-sizing:border-box;margin:0;padding:0}
html,body{width:1200px;height:5118px;overflow:hidden}
body{font-family:'Inter',sans-serif;color:var(--ink);background:var(--white);position:relative}
section,header,footer{position:relative;width:1200px}
.btn{display:inline-flex;align-items:center;justify-content:center;background:var(--red);color:var(--white);font-size:13px;font-weight:600;border-radius:4px}
.accent{display:flex;align-items:center;width:130px;height:24px}
.accent svg{display:block}
.h2{font-size:35px;font-weight:700;line-height:1.3;color:var(--ink)}
.p{font-size:12.5px;line-height:22px;color:var(--muted)}

/* header */
.site-header{height:96px;background:var(--white);z-index:5}
.brand-badge{position:absolute;left:113px;top:0;width:166px;height:190px;background:var(--white);clip-path:polygon(0 0,100% 0,100% 78%,50% 100%,0 78%);display:flex;flex-direction:column;align-items:center;justify-content:center;padding-bottom:40px;z-index:6}
.brand-badge .mark{width:56px;height:56px;border-radius:50%;background:var(--navy);margin-bottom:10px}
.brand-name{font-size:13px;font-weight:700;color:var(--navy);text-align:center;line-height:1.3;width:120px}
.nav{position:absolute;left:496px;top:40px;display:flex;gap:30px;font-size:13px;color:var(--ink)}
.nav a{position:relative}
.nav a.active:after{content:"";position:absolute;left:0;right:0;top:24px;height:2px;background:var(--red)}
.header-cta{position:absolute;left:942px;top:29px;width:190px;height:44px}

/* hero */
.hero{height:518px;background:linear-gradient(100deg,#1a2d55 0%,#223a68 40%,#2c4878 70%,#1e3052 100%)}
.hero .photo{position:absolute;inset:0}
.hero h1{position:absolute;left:115px;top:160px;font-size:50px;line-height:62px;font-weight:700;color:var(--white)}
.hero p{position:absolute;left:115px;top:308px;width:500px;font-size:12.5px;line-height:21px;color:#d8deea}
.hero .btn{position:absolute;left:119px;top:390px;width:248px;height:44px}

/* about */
.about{height:712px}
.about .h2{position:absolute;left:119px;top:100px;width:460px;line-height:48px}
.about .accent{position:absolute;left:119px;top:196px}
.about .copy{position:absolute;left:119px;top:236px;width:430px}
.about .copy p+p{margin-top:22px}
.link{font-size:13px;font-weight:500;color:var(--red);display:inline-flex;align-items:center;gap:8px}
.about .link{position:absolute;left:119px;top:452px}
.about .photo{position:absolute;left:656px;top:96px;width:406px;height:496px;background:linear-gradient(135deg,#1e2a3c 0%,#3a4656 30%,#c9ccd2 55%,#eef0f3 100%)}
.stats{position:absolute;left:204px;top:541px;display:flex;gap:16px}
.stat{width:186px;height:110px;background:var(--white);border:1px solid var(--line);box-shadow:0 6px 18px rgba(0,0,0,.05);padding:26px 26px}
.stat b{display:block;font-size:27px;font-weight:700;color:var(--ink)}
.stat span{display:block;margin-top:8px;font-size:10.5px;letter-spacing:.3px;color:var(--muted);white-space:nowrap}

/* capabilities */
.caps{height:558px;background:var(--soft)}
.center-head{position:absolute;left:0;width:1200px;text-align:center}
.center-head .sub{font-size:13px;color:var(--muted);margin-top:14px}
.center-head .accent{margin:16px auto 0;width:240px}
.caps .center-head{top:56px}
.cap-grid{position:absolute;left:99px;top:188px;display:flex;gap:28px}
.cap-card{width:229px;height:290px;background:var(--white);box-shadow:0 4px 14px rgba(0,0,0,.04);padding:28px 26px}
.icon-box{width:44px;height:44px;border-radius:4px;background:var(--red);display:flex;align-items:center;justify-content:center}
.cap-card h3{margin-top:22px;font-size:16px;font-weight:600;line-height:23px;color:var(--ink)}
.cap-card p{margin-top:12px;font-size:11.5px;line-height:19px;color:var(--muted)}

/* why */
.why{height:898px}
.why .photo{position:absolute;left:111px;top:85px;width:475px;height:718px;background:linear-gradient(160deg,#dfe4ea 0%,#b9c2cc 40%,#c7a24a 70%,#8d8a6a 100%)}
.why .h2{position:absolute;left:650px;top:108px;width:420px;line-height:48px}
.why .accent{position:absolute;left:650px;top:204px}
.timeline{position:absolute;left:670px;top:278px;width:1px;height:570px;border-left:1px dashed #c9ccd2}
.why-item{position:absolute;left:648px;width:460px}
.why-item .dot{position:absolute;left:0;top:0;width:44px;height:44px;border-radius:50%;background:var(--red);display:flex;align-items:center;justify-content:center;box-shadow:0 0 0 6px #fbe3e7}
.why-item h3{margin-left:64px;padding-top:12px;font-size:15px;font-weight:600;color:var(--ink)}
.why-item p{margin-left:64px;margin-top:10px;font-size:12.5px;line-height:21px;color:var(--muted)}

/* projects */
.projects{height:825px;background:var(--navy)}
.projects .h2{position:absolute;left:106px;top:78px;color:var(--white)}
.projects .accent{position:absolute;left:106px;top:136px}
.projects .intro{position:absolute;left:804px;top:80px;width:270px;font-size:12.5px;line-height:21px;color:#d9dee8}
.projects .link{position:absolute;left:804px;top:146px;color:var(--white)}
.slide-side{position:absolute;top:193px;height:487px}
.slide-left{left:111px;width:191px;background:linear-gradient(180deg,#2a3e5a 0%,#54708e 50%,#9aa9b8 100%)}
.slide-right{left:896px;width:193px;background:linear-gradient(180deg,#6a8098 0%,#b9a98c 50%,#48607c 100%)}
.slide-main{position:absolute;left:316px;top:193px;width:568px;height:487px;background:var(--navy-2)}
.slide-main .photo{height:258px;background:linear-gradient(180deg,#7fb0d8 0%,#4d7a58 55%,#2f5b35 100%)}
.slide-body{padding:30px 28px}
.slide-body .cat{font-size:11px;letter-spacing:.6px;color:#9aa6bb}
.slide-body h3{margin-top:14px;font-size:16px;font-weight:600;color:var(--white)}
.slide-body p{margin-top:16px;font-size:11.5px;line-height:20px;color:#c9d0dc}
.slide-body .meta{margin-top:10px;font-size:11.5px;line-height:24px;color:#aeb7c6}
.slide-body .meta b{color:#dfe4ec;font-weight:600}
.arrows{position:absolute;left:539px;top:706px;display:flex;gap:20px}
.arrow{width:50px;height:50px;border-radius:50%;background:var(--white);display:flex;align-items:center;justify-content:center}

/* key data */
.keydata{height:711px}
.keydata .center-head{top:70px}
.data-grid{position:absolute;left:197px;top:208px;display:flex;gap:22px}
.data-card{width:254px;height:165px;background:var(--white);box-shadow:0 4px 18px rgba(0,0,0,.07);padding:28px 26px}
.data-card h4{margin-top:18px;font-size:14px;font-weight:600}
.data-card .val{margin-top:6px;font-size:20px;font-weight:700;color:var(--red)}
.data-card small{display:block;margin-top:8px;font-size:11px;color:var(--muted)}
.naics-box{position:absolute;left:197px;top:393px;width:806px;height:246px;background:var(--white);box-shadow:0 4px 18px rgba(0,0,0,.07);padding:30px 26px}
.naics-box h4{font-size:14px;font-weight:600}
.naics{display:flex;margin-top:12px;border-bottom:1px solid var(--line);padding-bottom:20px}
.naics div{width:250px;padding-right:18px}
.naics div:nth-child(3){margin-top:16px}
.naics b{display:block;font-size:14px;font-weight:700;color:var(--red)}
.naics span{display:block;margin-top:4px;font-size:11px;line-height:15px;color:var(--muted)}
.certs{display:flex;margin-top:18px}
.cert-col{width:422px}
.cert-col+.cert-col{border-left:1px solid var(--line);padding-left:22px;width:360px}
.cert-row{display:flex;gap:36px;margin-top:18px}
.cert{display:flex;gap:10px;align-items:flex-start}
.cert b{display:block;font-size:11.5px;font-weight:600}
.cert span{display:block;font-size:10px;color:var(--muted);margin-top:2px}

/* cta */
.cta{height:411px;background:linear-gradient(180deg,#f4f6f9 0%,#e6ebf1 100%)}
.cta .bg{position:absolute;inset:0}
.cta .center-head{top:110px}
.cta .center-head p{width:440px;margin:20px auto 0;font-size:13px;line-height:21px;color:var(--muted)}
.cta .btn{position:absolute;left:516px;top:272px;width:168px;height:44px}

/* footer */
.site-footer{height:389px;background:var(--navy)}
.footer-badge{position:absolute;left:79px;top:-70px;width:166px;height:190px;background:var(--white);clip-path:polygon(0 0,100% 0,100% 78%,50% 100%,0 78%);display:flex;flex-direction:column;align-items:center;justify-content:center;padding-bottom:36px}
.footer-badge .mark{width:56px;height:56px;border-radius:50%;background:var(--navy);margin-bottom:10px}
.footer-about{position:absolute;left:81px;top:144px;width:350px;font-size:11.5px;line-height:20px;color:#aeb7c6}
.contact{position:absolute;left:81px;top:224px;font-size:11.5px;color:#c3cad6}
.contact li{list-style:none;display:flex;gap:12px;line-height:18px;margin-bottom:10px}
.fcol{position:absolute;top:95px;font-size:11.5px;color:#aeb7c6}
.fcol h5{font-size:11px;font-weight:700;letter-spacing:.8px;color:var(--white);margin-bottom:18px}
.fcol li{list-style:none;margin-bottom:14px}
.footer-bottom{position:absolute;left:87px;right:87px;top:354px;display:flex;justify-content:space-between;font-size:11px;color:#aeb7c6}
.footer-bottom nav{display:flex;gap:14px}
</style>
</head>
<body>

<header class="site-header">
  <div class="brand-badge">
    <div class="mark"></div>
    <div class="brand-name">R5 Construction USA</div>
  </div>
  <nav class="nav">
    <a class="active">Home</a><a>About</a><a>Services</a><a>Projects</a><a>Contact</a>
  </nav>
  <a class="btn header-cta">Capability Statement</a>
</header>

<section class="hero">
  <div class="photo" role="img" aria-label="Blue-toned photo of a modern high-rise building under construction"></div>
  <h1>Federal Contracting<br>You Can Trust</h1>
  <p>Two generations of proven experience delivering reliable general contracting solutions for government and commercial projects nationwide.</p>
  <a class="btn">Request Capability Statement</a>
</section>

<section class="about">
  <h2 class="h2">A Legacy of Excellence<br>in Federal Contracting</h2>
  <div class="accent"><svg width="130" height="24" viewBox="0 0 130 24"><polygon points="12,2 14.8,9 22,9 16.2,13.5 18.4,21 12,16.5 5.6,21 7.8,13.5 2,9 9.2,9" fill="#c81f3c"/><path d="M24 12 L130 12" stroke="#c81f3c" stroke-width="2"/></svg></div>
  <div class="copy p">
    <p>For over four decades, Liberty Ridge Contracting Group has been a trusted partner to federal agencies and government entities across the United States. Our commitment to quality, compliance, and mission success spans two generations of dedicated service.</p>
    <p>We understand the unique demands of government contracting—from stringent regulatory requirements to the critical importance of on-time, on-budget delivery. Our experience and reputation speak for themselves.</p>
  </div>
  <a class="link">Learn More About Us <svg width="16" height="16" viewBox="0 0 16 16"><circle cx="8" cy="8" r="8" fill="#c81f3c"/><path d="M5.5 10.5 L10.5 5.5 M7 5.5 H10.5 V9" stroke="#fff" stroke-width="1.5" fill="none"/></svg></a>
  <div class="photo" role="img" aria-label="Close-up photo of a hand sketching on architectural blueprints with a pencil"></div>
  <div class="stats">
    <div class="stat"><b>40+</b><span>YEARS EXPERIENCE</span></div>
    <div class="stat"><b>500+</b><span>PROJECTS COMPLETED</span></div>
    <div class="stat"><b>$2B+</b><span>CONTRACT VALUE</span></div>
    <div class="stat"><b>98%</b><span>CLIENT RETENTION</span></div>
  </div>
</section>

<section class="caps">
  <div class="center-head">
    <h2 class="h2">Core Capabilities</h2>
    <p class="sub">Comprehensive construction and contracting services tailored for federal requirements</p>
    <div class="accent"><svg width="240" height="24" viewBox="0 0 240 24"><path d="M0 12 H106 M134 12 H240" stroke="#c81f3c" stroke-width="2"/><polygon points="120,2 122.8,9 130,9 124.2,13.5 126.4,21 120,16.5 113.6,21 115.8,13.5 110,9 117.2,9" fill="#c81f3c"/></svg></div>
  </div>
  <div class="cap-grid">
    <article class="cap-card">
      <div class="icon-box"><svg width="20" height="20" viewBox="0 0 20 20" fill="none" stroke="#fff" stroke-width="1.6"><rect x="4" y="2" width="12" height="16" rx="1"/><path d="M7 6h6M7 10h6M7 14h4"/></svg></div>
      <h3>General<br>Contracting</h3>
      <p>Full-service construction management from design through completion, ensuring quality and compliance at every phase.</p>
    </article>
    <article class="cap-card">
      <div class="icon-box"><svg width="20" height="20" viewBox="0 0 20 20" fill="none" stroke="#fff" stroke-width="1.6"><path d="M2 8 L10 3 L18 8 Z M4 8v8 M8 8v8 M12 8v8 M16 8v8 M2 17h16"/></svg></div>
      <h3>Federal Contracting</h3>
      <p>Specialized expertise in navigating federal procurement processes, FAR compliance, and government project delivery.</p>
    </article>
    <article class="cap-card">
      <div class="icon-box"><svg width="20" height="20" viewBox="0 0 20 20" fill="none" stroke="#fff" stroke-width="1.6"><rect x="4" y="3" width="12" height="15" rx="1"/><path d="M7 11l2 2 4-4"/></svg></div>
      <h3>Project<br>Management</h3>
      <p>Comprehensive oversight ensuring projects meet scope, schedule, and budget requirements with rigorous quality control.</p>
    </article>
    <article class="cap-card">
      <div class="icon-box"><svg width="20" height="20" viewBox="0 0 20 20" fill="none" stroke="#fff" stroke-width="1.6"><path d="M12 3a4 4 0 0 0 4 5l-9 9-3-3 9-9a4 4 0 0 1-1-2z"/></svg></div>
      <h3>Construction<br>Services</h3>
      <p>New construction, renovation, repair, and maintenance services for federal facilities and infrastructure projects.</p>
    </article>
  </div>
</section>

<section class="why">
  <div class="photo" role="img" aria-label="Photo of a construction supervisor in a hard hat and safety vest reviewing a tablet in front of a high-rise site"></div>
  <h2 class="h2">Why Federal<br>Agencies Choose Us</h2>
  <div class="accent"><svg width="130" height="24" viewBox="0 0 130 24"><polygon points="12,2 14.8,9 22,9 16.2,13.5 18.4,21 12,16.5 5.6,21 7.8,13.5 2,9 9.2,9" fill="#c81f3c"/><path d="M24 12 L130 12" stroke="#c81f3c" stroke-width="2"/></svg></div>
  <div class="timeline"></div>
  <div class="why-item" style="top:278px">
    <div class="dot"><svg width="18" height="18" viewBox="0 0 18 18" fill="none" stroke="#fff" stroke-width="1.5"><circle cx="7" cy="6" r="3"/><path d="M2 15c0-3 2-5 5-5s5 2 5 5M12 3a3 3 0 0 1 0 6M14 10c1.5.7 2 2.5 2 5"/></svg></div>
    <h3>Two Generations of Experience</h3>
    <p>Our family-owned business brings continuity, institutional knowledge, and a long-term commitment to excellence that sets us apart from competitors.</p>
  </div>
  <div class="why-item" style="top:411px">
    <div class="dot"><svg width="18" height="18" viewBox="0 0 18 18" fill="none" stroke="#fff" stroke-width="1.5"><path d="M9 2l6 2.5v4.5c0 3.5-2.5 6-6 7-3.5-1-6-3.5-6-7V4.5z"/></svg></div>
    <h3>Government Expertise</h3>
    <p>Deep understanding of federal regulations, procurement processes, and security requirements ensures seamless project execution and compliance.</p>
  </div>
  <div class="why-item" style="top:544px">
    <div class="dot"><svg width="18" height="18" viewBox="0 0 18 18" fill="none" stroke="#fff" stroke-width="1.5"><circle cx="9" cy="9" r="7"/><path d="M6 9l2 2 4-4"/></svg></div>
    <h3>Reliable Delivery</h3>
    <p>Proven track record of on-time, on-budget project completion with zero contract defaults and consistently high performance ratings.</p>
  </div>
  <div class="why-item" style="top:685px">
    <div class="dot"><svg width="18" height="18" viewBox="0 0 18 18" fill="none" stroke="#fff" stroke-width="1.5"><circle cx="9" cy="7" r="4"/><path d="M6.5 10.5L5.5 16l3.5-2 3.5 2-1-5.5"/></svg></div>
    <h3>Compliance Standards</h3>
    <p>Rigorous adherence to FAR, DFARS, safety protocols, and quality standards with comprehensive documentation and reporting systems.</p>
  </div>
</section>

<section class="projects">
  <h2 class="h2">Core Capabilities</h2>
  <div class="accent"><svg width="130" height="24" viewBox="0 0 130 24"><polygon points="12,2 14.8,9 22,9 16.2,13.5 18.4,21 12,16.5 5.6,21 7.8,13.5 2,9 9.2,9" fill="#c81f3c"/><path d="M24 12 L130 12" stroke="#c81f3c" stroke-width="2"/></svg></div>
  <p class="intro">Representative projects demonstrating our capability and reliability</p>
  <a class="link">View All Projects <svg width="16" height="16" viewBox="0 0 16 16"><circle cx="8" cy="8" r="8" fill="#c81f3c"/><path d="M5.5 10.5 L10.5 5.5 M7 5.5 H10.5 V9" stroke="#fff" stroke-width="1.5" fill="none"/></svg></a>
  <div class="slide-side slide-left" role="img" aria-label="Photo of a modern dark glass office building"></div>
  <article class="slide-main">
    <div class="photo" role="img" aria-label="Photo of a glass-walled government facility surrounded by trees and landscaping"></div>
    <div class="slide-body">
      <div class="cat">DEPARTMENT OF DEFENSE</div>
      <h3>Military Base Renovation</h3>
      <p>Complete renovation of 125,000 sq ft facility including barracks, administrative offices, and training spaces.</p>
      <div class="meta"><b>Contract Value:</b> $45M<br><b>Duration:</b> 18 months<br><b>Rating:</b> Exceptional (95/100)</div>
    </div>
  </article>
  <div class="slide-side slide-right" role="img" aria-label="Photo of a stone bank building facade"></div>
  <div class="arrows">
    <div class="arrow"><svg width="14" height="14" viewBox="0 0 14 14" fill="none" stroke="#14213a" stroke-width="1.8"><path d="M9 2L4 7l5 5"/></svg></div>
    <div class="arrow"><svg width="14" height="14" viewBox="0 0 14 14" fill="none" stroke="#14213a" stroke-width="1.8"><path d="M5 2l5 5-5 5"/></svg></div>
  </div>
</section>

<section class="keydata">
  <div class="center-head">
    <h2 class="h2">Key Data &amp; Certifications</h2>
    <p class="sub">Comprehensive construction and contracting services tailored for federal requirements</p>
    <div class="accent"><svg width="240" height="24" viewBox="0 0 240 24"><path d="M0 12 H106 M134 12 H240" stroke="#c81f3c" stroke-width="2"/><polygon points="120,2 122.8,9 130,9 124.2,13.5 126.4,21 120,16.5 113.6,21 115.8,13.5 110,9 117.2,9" fill="#c81f3c"/></svg></div>
  </div>
  <div class="data-grid">
    <div class="data-card"><svg width="20" height="22" viewBox="0 0 20 22" fill="none" stroke="#1a1d24" stroke-width="1.5"><path d="M4 1h8l5 5v15H4z M12 1v5h5 M7 11h7 M7 15h7"/></svg><h4>DUNS Number</h4><div class="val">123456789</div><small>UEI: ABCDEFGH1234</small></div>
    <div class="data-card"><svg width="20" height="22" viewBox="0 0 20 22" fill="none" stroke="#1a1d24" stroke-width="1.5"><path d="M4 1h8l5 5v15H4z M12 1v5h5 M7 11h7 M7 15h7"/></svg><h4>CAGE Code</h4><div class="val">1AB23</div><small>Registered &amp; Active</small></div>
    <div class="data-card"><svg width="20" height="22" viewBox="0 0 20 22" fill="none" stroke="#1a1d24" stroke-width="1.5"><path d="M4 1h8l5 5v15H4z M12 1v5h5 M7 11h7 M7 15h7"/></svg><h4>SAM Registration</h4><div class="val">Active</div><small>Expires: March 2027</small></div>
  </div>
  <div class="naics-box">
    <h4>Primary NAICS Codes</h4>
    <div class="naics">
      <div><b>236220</b><span>Commercial and Institutional Building Construction</span></div>
      <div style="margin-top:16px"><b>237310</b><span>Highway, Street, and Bridge Construction</span></div>
      <div><b>238990</b><span>All Other Specialty Trade Contractors</span></div>
    </div>
    <div class="certs">
      <div class="cert-col">
        <h4>Certifications &amp; Clearances</h4>
        <div class="cert-row">
          <div class="cert"><svg width="16" height="16" viewBox="0 0 16 16" fill="none" stroke="#1a1d24" stroke-width="1.5"><circle cx="8" cy="8" r="6.5"/><path d="M5 8l2 2 4-4"/></svg><div><b>ISO 9001:2015</b><span>Quality Management</span></div></div>
          <div class="cert"><svg width="16" height="16" viewBox="0 0 16 16" fill="none" stroke="#1a1d24" stroke-width="1.5"><path d="M8 1.5l5.5 2v4c0 3.5-2.5 5.5-5.5 7-3-1.5-5.5-3.5-5.5-7v-4z"/></svg><div><b>OSHA Certified</b><span>Safety Compliance</span></div></div>
        </div>
      </div>
      <div class="cert-col">
        <h4>Certifications &amp; Clearances</h4>
        <div class="cert-row">
          <div class="cert"><svg width="16" height="16" viewBox="0 0 16 16" fill="none" stroke="#1a1d24" stroke-width="1.5"><rect x="3" y="7" width="10" height="8" rx="1"/><path d="M5 7V5a3 3 0 0 1 6 0v2"/></svg><div><b>Secret Clearance</b><span>Facility &amp; Personnel</span></div></div>
          <div class="cert"><svg width="16" height="16" viewBox="0 0 16 16" fill="none" stroke="#1a1d24" stroke-width="1.5"><circle cx="8" cy="8" r="6.5"/><polygon points="8,4.5 9,7 11.5,7 9.5,8.6 10.2,11 8,9.6 5.8,11 6.5,8.6 4.5,7 7,7" fill="#1a1d24" stroke="none"/></svg><div><b>8(a) Eligible</b><span>Small Business Program</span></div></div>
        </div>
      </div>
    </div>
  </div>
</section>

<section class="cta">
  <div class="bg" role="img" aria-label="Faded photo of city buildings and rolled construction plans on a desk"></div>
  <div class="center-head">
    <h2 class="h2">Key Data &amp; Certifications</h2>
    <div class="accent"><svg width="240" height="24" viewBox="0 0 240 24"><path d="M0 12 H106 M134 12 H240" stroke="#c81f3c" stroke-width="2"/><polygon points="120,2 122.8,9 130,9 124.2,13.5 126.4,21 120,16.5 113.6,21 115.8,13.5 110,9 117.2,9" fill="#c81f3c"/></svg></div>
    <p>Partner with a contractor that understands federal requirements and delivers results. Contact us today to discuss your project needs.</p>
  </div>
  <a class="btn">Contact Us Today</a>
</section>

<footer class="site-footer">
  <div class="footer-badge">
    <div class="mark"></div>
    <div class="brand-name">R5 Construction USA</div>
  </div>
  <p class="footer-about">Two generations of proven experience delivering reliable general contracting solutions for government and commercial projects nationwide.</p>
  <ul class="contact">
    <li><svg width="12" height="14" viewBox="0 0 12 14" fill="none" stroke="#c3cad6" stroke-width="1.3"><path d="M6 13s5-4.5 5-8A5 5 0 0 0 1 5c0 3.5 5 8 5 8z"/><circle cx="6" cy="5" r="1.8"/></svg><span>4820 Liberty Avenue, Suite 300<br>Arlington, VA 22201</span></li>
    <li><svg width="13" height="13" viewBox="0 0 13 13" fill="none" stroke="#c3cad6" stroke-width="1.3"><path d="M2 1h3l1 3-1.5 1a7 7 0 0 0 3.5 3.5L9 7l3 1v3a1 1 0 0 1-1 1A10 10 0 0 1 1 2a1 1 0 0 1 1-1z"/></svg><span>(703) 555-0147</span></li>
    <li><svg width="13" height="11" viewBox="0 0 13 11" fill="none" stroke="#c3cad6" stroke-width="1.3"><rect x="1" y="1" width="11" height="9" rx="1"/><path d="M1 2l5.5 4L12 2"/></svg><span>info@libertyridgebuild.com</span></li>
  </ul>
  <div class="fcol" style="left:660px">
    <h5>QUICK LINKS</h5>
    <ul><li>Home</li><li>About Us</li><li>Services</li><li>Projects</li><li>Contact</li></ul>
  </div>
  <div class="fcol" style="left:874px">
    <h5>RESOURCES</h5>
    <ul><li>Capability Statement</li><li>Secure Access</li><li>Compliance &amp; Certifications</li><li>Past Performance</li></ul>
  </div>
  <div class="footer-bottom">
    <span>© 2026 Liberty Ridge Contracting Group. All rights reserved.</span>
    <nav><a>Privacy Policy</a><a>Terms of Service</a></nav>
  </div>
</footer>

</body>
</html>
```